Independent Financial Advisor Billboard Campaign - Granite Bridge Financial

I am a local, independent financial advisor. My company is Granite Bridge Financial, located in Charleston, WV. My main source of revenue comes from those nearing or entering retirement that need assistance with financial planning and investment management. Many are looking to rollover their employer retirement plan into an IRA account. I would like a billboard design campaign that focuses on this type of client. Please see our website www.granitebridgefinancial-example.com for more information.

```html
<!DOCTYPE html>
<html lang="en">
<head>
<meta charset="utf-8">
<title>Granite Bridge Financial – Retirement Billboard</title>
<link rel="stylesheet" href="https://fonts.googleapis.com/css2?family=Cinzel:wght@500;600&family=Poppins:wght@500;700&display=swap">
<style>
  :root {
    --page-bg: #8f8f8f;
    --brand-blue: #17467f;
    --accent-blue: #3d8fe0;
    --slate-gray: #8a8a8a;
    --headline-gray: #5a5a5a;
    --panel-light: #f3f3f3;
    --panel-mid: #e2e2e2;
    --band-dark: #262626;
    --white: #ffffff;
  }
  html, body {
    margin: 0;
    padding: 0;
    width: 1196px;
    height: 1200px;
    overflow: hidden;
    background: var(--page-bg);
  }
  .canvas {
    position: relative;
    width: 1196px;
    height: 1200px;
  }
  .billboard {
    position: absolute;
    left: 48px;
    top: 440px;
    width: 1100px;
    height: 321px;
    box-shadow: 0 10px 22px rgba(0,0,0,0.35);
    display: block;
  }
  .headline {
    font-family: "Cinzel", "Times New Roman", serif;
    font-weight: 500;
  }
  .headline-top { fill: var(--brand-blue); }
  .headline-bottom { fill: var(--headline-gray); }
  .phone-number {
    font-family: "Poppins", Arial, sans-serif;
    font-weight: 700;
    fill: var(--white);
  }
  .web-address {
    font-family: "Poppins", Arial, sans-serif;
    font-weight: 500;
    fill: var(--white);
  }
  .web-address .web-name { fill: var(--accent-blue); }
  .brand-name {
    font-family: "Cinzel", "Times New Roman", serif;
    font-weight: 600;
    fill: var(--brand-blue);
  }
</style>
</head>
<body>
<main class="canvas">
  <svg class="billboard" viewBox="0 0 1320 385" xmlns="http://www.w3.org/2000/svg">
    <defs>
      <linearGradient id="backdropTone" x1="0" y1="0" x2="1" y2="1">
        <stop offset="0" stop-color="#f7f7f7"/>
        <stop offset="0.6" stop-color="#eaeaea"/>
        <stop offset="1" stop-color="#dcdcdc"/>
      </linearGradient>
      <linearGradient id="portraitTone" x1="0" y1="0" x2="0" y2="1">
        <stop offset="0" stop-color="#d9b49a"/>
        <stop offset="0.45" stop-color="#e8ddd6"/>
        <stop offset="1" stop-color="#f4f4f4"/>
      </linearGradient>
    </defs>

    <!-- backdrop -->
    <rect class="backdrop" x="0" y="0" width="1320" height="385" fill="var(--panel-light)"/>
    <rect class="backdrop-photo" x="320" y="0" width="1000" height="355" fill="url(#backdropTone)" role="img" aria-label="Faded photo of a smiling retired couple"/>

    <!-- left stripes -->
    <polygon class="stripe-gray" points="0,0 45,0 110,385 0,385" fill="var(--slate-gray)"/>
    <polygon class="stripe-blue" points="45,0 270,0 330,385 105,385" fill="var(--brand-blue)"/>
    <polygon class="stripe-gray-right" points="272,0 325,0 368,225 312,225" fill="var(--slate-gray)" stroke="var(--white)" stroke-width="4"/>

    <!-- advisor portrait -->
    <rect class="advisor-portrait" x="0" y="20" width="345" height="365" fill="url(#portraitTone)" role="img" aria-label="Portrait of the advisor in a white polo shirt"/>

    <!-- contact panel -->
    <polygon class="contact-panel" points="318,225 842,225 897,385 345,385" fill="var(--brand-blue)" stroke="var(--white)" stroke-width="4"/>
    <polygon class="bottom-band" points="885,353 1320,353 1320,385 896,385" fill="var(--band-dark)"/>

    <!-- headline -->
    <text class="headline headline-top" x="402" y="116" font-size="106" textLength="708" lengthAdjust="spacingAndGlyphs">RETIREMENT</text>
    <text class="headline headline-bottom" x="402" y="202" font-size="106" textLength="752" lengthAdjust="spacingAndGlyphs">DONE RIGHT!</text>

    <!-- phone -->
    <g class="phone-icon" transform="translate(385,278)">
      <circle r="21" fill="var(--accent-blue)"/>
      <path d="M-9,-11 l6,-2 l4,8 l-4,3 q3,7 9,10 l3,-4 l8,4 l-2,6 q-3,3 -8,1 q-13,-6 -18,-18 q-1,-5 2,-8z" fill="var(--white)"/>
    </g>
    <text class="phone-number" x="418" y="300" font-size="56" textLength="385" lengthAdjust="spacingAndGlyphs">304.555.0142</text>
    <text class="web-address" x="367" y="334" font-size="21" textLength="475" lengthAdjust="spacingAndGlyphs">www.<tspan class="web-name">granitebridgefinancial-example</tspan>.com</text>

    <!-- brand -->
    <rect class="brand-mark" x="872" y="262" width="56" height="56" fill="var(--brand-blue)"/>
    <text class="brand-name" x="942" y="286" font-size="30">Granite Bridge</text>
    <text class="brand-name" x="942" y="322" font-size="30">Financial</text>
  </svg>
</main>
</body>
</html>
```